Protrait photographers business card

Need a new catchy, chic business card to promote my new portrait photograghy business. Love taking the natural, location portraits of families, children, teens. It should look classy, but also warm & friendly. I want it to show that Famliy, friends, couples & childten are what I love photographing, so if it can have that sort of feel to it & also looking energetic.

Target Market(s)

Families, couples, babies, people on holidays wanting some locational professional photos

Industry/Entity Type

Portrait Photography

Contact Information for Business Card

Lumivale photography, By Tavi, Norah Balfrey,Ph: 0487356024, Kestrel cove, Qld

Font styles to use
Decorative
Script

Requirements
Must have
• Company name & photographers name
Nice to have
• a coloured card
Should not have
• not be on a white card

```html
<!DOCTYPE html>
<html lang="en">
<head>
<meta charset="utf-8">
<title>Lumivale photography – business card</title>
<link rel="stylesheet" href="https://fonts.googleapis.com/css2?family=Open+Sans:wght@400;600;700&display=swap">
<style>
  :root {
    --page-bg: #e9e6e1;
    --card-white: #ffffff;
    --band-blue: #27a5df;
    --band-blue-light: #4bb8e8;
    --stripe-green: #3aa66a;
    --brand-blue: #6cc3e6;
    --ink-grey: #555a5e;
    --ink-white: #ffffff;
  }
  * { margin: 0; padding: 0; box-sizing: border-box; }
  html, body {
    width: 1200px;
    height: 902px;
    overflow: hidden;
    background: var(--page-bg);
    font-family: "Open Sans", Arial, sans-serif;
  }
  .canvas {
    width: 1200px;
    height: 902px;
    display: flex;
    align-items: center;
    justify-content: center;
  }
  .business-card {
    position: relative;
    width: 900px;
    height: 514px;
    background: var(--card-white);
    overflow: hidden;
    box-shadow: 0 14px 40px rgba(0, 0, 0, 0.18);
  }
  .brand {
    position: absolute;
    top: 96px;
    left: 0;
    right: 0;
    display: flex;
    align-items: center;
    justify-content: center;
    gap: 18px;
  }
  .brand-dot {
    width: 34px;
    height: 34px;
    border-radius: 50%;
    background: var(--brand-blue);
  }
  .brand-name {
    font-size: 46px;
    font-weight: 400;
    color: var(--brand-blue);
    letter-spacing: 0.5px;
  }
  .location {
    position: absolute;
    left: 56px;
    top: 232px;
    display: flex;
    align-items: center;
    gap: 12px;
    font-size: 22px;
    color: var(--ink-grey);
  }
  .stripe {
    position: absolute;
    left: 0;
    right: 0;
    top: 282px;
    height: 12px;
    background: var(--stripe-green);
  }
  .band {
    position: absolute;
    left: 0;
    right: 0;
    top: 294px;
    bottom: 0;
    background: linear-gradient(100deg, var(--band-blue-light) 0%, var(--band-blue) 40%, var(--band-blue) 100%);
  }
  .contact-list {
    position: absolute;
    right: 70px;
    top: 18px;
    list-style: none;
    color: var(--ink-white);
    font-size: 20px;
    line-height: 36px;
  }
  .contact-list li {
    display: flex;
    align-items: center;
    gap: 14px;
  }
  .contact-list svg { flex: none; }
  .photographer {
    position: absolute;
    left: 56px;
    bottom: 44px;
    color: var(--ink-white);
  }
  .photographer-tag {
    font-size: 34px;
    font-weight: 700;
    line-height: 1.1;
  }
  .photographer-name {
    font-size: 28px;
    font-weight: 400;
    line-height: 1.2;
  }
</style>
</head>
<body>
<main class="canvas">
  <section class="business-card">
    <div class="brand">
      <span class="brand-dot"></span>
      <span class="brand-name">Lumivale photography</span>
    </div>

    <p class="location">
      <svg width="16" height="22" viewBox="0 0 16 22" aria-hidden="true">
        <path d="M8 0C3.6 0 0 3.5 0 7.8 0 13.5 8 22 8 22s8-8.5 8-14.2C16 3.5 12.4 0 8 0z" fill="var(--brand-blue)"/>
        <circle cx="8" cy="7.8" r="3" fill="#fff"/>
      </svg>
      Kestrel cove, Qld
    </p>

    <div class="stripe"></div>

    <div class="band">
      <ul class="contact-list">
        <li>
          <svg width="20" height="20" viewBox="0 0 24 24" aria-hidden="true">
            <path d="M6.6 10.8a15.1 15.1 0 0 0 6.6 6.6l2.2-2.2a1 1 0 0 1 1-.25 11.4 11.4 0 0 0 3.6.57 1 1 0 0 1 1 1V20a1 1 0 0 1-1 1A17 17 0 0 1 3 4a1 1 0 0 1 1-1h3.5a1 1 0 0 1 1 1c0 1.25.2 2.45.57 3.57a1 1 0 0 1-.25 1z" fill="#fff"/>
          </svg>
          0487356024
        </li>
        <li>
          <svg width="20" height="20" viewBox="0 0 24 24" aria-hidden="true">
            <circle cx="12" cy="12" r="10" fill="none" stroke="#fff" stroke-width="2"/>
            <ellipse cx="12" cy="12" rx="4.5" ry="10" fill="none" stroke="#fff" stroke-width="1.6"/>
            <line x1="2" y1="12" x2="22" y2="12" stroke="#fff" stroke-width="1.6"/>
            <line x1="4" y1="7" x2="20" y2="7" stroke="#fff" stroke-width="1.4"/>
            <line x1="4" y1="17" x2="20" y2="17" stroke="#fff" stroke-width="1.4"/>
          </svg>
          www.lumivale.com
        </li>
        <li>
          <svg width="20" height="20" viewBox="0 0 24 24" aria-hidden="true">
            <text x="12" y="18" text-anchor="middle" font-family="Open Sans, Arial, sans-serif" font-size="20" font-weight="700" fill="#fff">@</text>
          </svg>
          info@lumivale.com
        </li>
      </ul>

      <div class="photographer">
        <p class="photographer-tag">By Tavi</p>
        <p class="photographer-name">Norah Balfrey</p>
      </div>
    </div>
  </section>
</main>
</body>
</html>
```